BUSINESS CARD DESIGN

NAME- TODD MASVERIK
PHONE NUMER - 808- 451-7082
EMAIL- OFFICE@VORLINDE-GRADEWAY.COM
BACK OF CARD- SPEACIALIZES IN LAND CLEARING, FORESTRY MUCLHING AND EXCAVATION

Contact Information for Business Card

NAME- TODD MASVERIK PHONE NUMER - 808- 451-7082 EMAIL- OFFICE@VORLINDE-GRADEWAY.COM BACK OF CARD- SPEACIALIZES IN LAND CLEARING , MUCLHING AND EXCAVATION

```html
<!DOCTYPE html>
<html lang="en">
<head>
<meta charset="utf-8">
<title>Vorlinde Gradeway LLC — Business Card</title>
<link href="https://fonts.googleapis.com/css2?family=Montserrat:wght@400;500&family=Lato:wght@700&display=swap" rel="stylesheet">
<style>
  :root {
    --backdrop: #6a6a6a;
    --card-front: #232323;
    --card-back: #000000;
    --gold: #f5bb12;
    --band-gold: #f2c31b;
    --white: #ffffff;
    --silver: #d9d9d9;
    --ink: #111111;
  }
  html, body {
    margin: 0;
    width: 1200px;
    height: 1000px;
    overflow: hidden;
    background: var(--backdrop);
  }
  .canvas { position: relative; width: 1200px; height: 1000px; }
  .card {
    position: absolute;
    left: 195px;
    width: 810px;
    height: 463px;
    border-radius: 18px;
    overflow: hidden;
  }
  .card-front { top: 30px; background: var(--card-front); }
  .card-back { top: 507px; background: var(--card-back); }

  .front-brand {
    position: absolute;
    left: 0; right: 0; top: 150px;
    display: flex; flex-direction: column; align-items: center; gap: 26px;
  }
  .brand-mark {
    width: 74px; height: 74px; border-radius: 50%;
    border: 5px solid var(--silver); box-sizing: border-box;
  }
  .front-brand .brand-name {
    font-family: "Montserrat", sans-serif; font-weight: 500;
    font-size: 40px; letter-spacing: 3px; color: var(--silver);
  }

  .back-brand {
    position: absolute; left: 45px; top: 100px; width: 240px;
    font-family: "Montserrat", sans-serif; font-weight: 500;
    font-size: 26px; line-height: 1.25; letter-spacing: 1px;
    color: var(--gold); text-align: center;
  }
  .person-name {
    position: absolute; left: 330px; top: 112px; margin: 0;
    font-family: "Montserrat", sans-serif; font-weight: 500;
    font-size: 29px; letter-spacing: 0.5px; color: var(--gold);
  }
  .contact-list {
    position: absolute; left: 325px; top: 186px; margin: 0; padding: 0;
    list-style: none;
    font-family: "Montserrat", sans-serif; font-weight: 400;
    color: var(--white);
  }
  .contact-item { display: flex; align-items: center; gap: 14px; height: 38px; }
  .contact-item svg { width: 26px; height: 26px; flex: none; }
  .contact-phone { font-size: 25px; }
  .contact-email { font-size: 21px; letter-spacing: 0.3px; }

  .services-band { position: absolute; left: 0; top: 305px; width: 810px; height: 52px; }
  .services-band svg { position: absolute; inset: 0; }
  .service {
    position: absolute; top: 0; height: 52px; display: flex; align-items: center; gap: 10px;
    font-family: "Lato", sans-serif; font-weight: 700; font-size: 18px; color: var(--ink);
  }
  .service::before { content: ""; width: 10px; height: 10px; border-radius: 50%; background: var(--ink); }
  .service-clearing { left: 95px; }
  .service-excavation { left: 430px; }
  .service-excavation::before { background: var(--band-gold); }
</style>
</head>
<body>
<div class="canvas">
  <section class="card card-front">
    <div class="front-brand">
      <div class="brand-mark"></div>
      <div class="brand-name">VORLINDE GRADEWAY LLC</div>
    </div>
  </section>

  <section class="card card-back">
    <div class="back-brand">VORLINDE GRADEWAY LLC</div>

    <h1 class="person-name">TODD MASVERIK</h1>
    <ul class="contact-list">
      <li class="contact-item contact-phone">
        <svg viewBox="0 0 24 24" aria-hidden="true"><path d="M6.6 3.5l2.6 3-1.6 2.2a12 12 0 0 0 5.7 5.7l2.2-1.6 3 2.6-1.4 3a2 2 0 0 1-2 1C9.3 19 5 14.7 4.5 8.9a2 2 0 0 1 1-2z" fill="none" stroke="#f5bb12" stroke-width="1.8" stroke-linejoin="round"/><path d="M14 3h7v5h-4l-2 2V8h-1z" fill="none" stroke="#f5bb12" stroke-width="1.5" stroke-linejoin="round"/></svg>
        808- 451-7082
      </li>
      <li class="contact-item contact-email">
        <svg viewBox="0 0 24 24" aria-hidden="true"><path d="M2 11L22 3l-6 19-4-8z" fill="#f5bb12"/><path d="M12 14L22 3" stroke="#000" stroke-width="1.2"/></svg>
        OFFICE@VORLINDE-GRADEWAY.COM
      </li>
    </ul>

    <div class="services-band">
      <svg viewBox="0 0 810 52" width="810" height="52" aria-hidden="true">
        <polygon points="0,0 425,0 390,52 0,52" fill="#f2c31b"/>
        <polygon points="432,0 810,0 810,52 397,52" fill="#ffffff"/>
      </svg>
      <span class="service service-clearing">Speacializes In Land Clearing</span>
      <span class="service service-excavation">Mulching And Excavation</span>
    </div>
  </section>
</div>
</body>
</html>
```